Business Card for Pottery and Jewellery Designer

A new business card design is needed to accompany a newly launching pottery and jewellery website. The company logo has been attached for use. The company is called Glazewick Studio. For a sense of the vibe please see the website (it is currently under construction but this way you'll get a feel for the style) www.GlazewickStudio.com

The website font is Pontano Sans for the body of the text with Overlock for headers.

The overall look should be clean and elegant. The back side can have just the logo. The front side should have a smaller logo and the following details displayed:

Glazewick Studio
Designer: Hollis Marrow
Phone: xxx.xxx.xxxx
Email: Designer@GlazewickStudio.com

The structure of displaying this is completely up to you. Different layouts and creative methods of displaying contact info are welcome as long as it stays clean/uncluttered.

No product photographs are to be included in the design as the catalogue changes quickly.

Colour preferences lean towards elegant and understated (charcoal grey, dark navy blue etc.)

Please let me know if you have any further questions or further details required.

Target Market(s)

Target market is 30+ year old women

Industry/Entity Type

Construction

Colors
ffffff
1b1b1b
474747
d9d9d9
fafafa
0355a3

Requirements
Must have
• The submissions so far have looked very typical and don't stand out right now. They're also all in navy with very little variation. I'm looking for something that stands out a it more while still being clean-looking.
Nice to have
• I've attached a few design samples and an idea for a backdrop. It would be great to see some designs in black, white, and grey with only a hint of color.
Should not have
• Product Images

```html
<!DOCTYPE html>
<html lang="en">
<head>
<meta charset="utf-8">
<title>Glazewick Studio — Business Card</title>
<link rel="stylesheet" href="https://fonts.googleapis.com/css2?family=Poiret+One&display=swap">
<style>
  :root {
    --white: #ffffff;
    --ink: #1b1b1b;
    --charcoal: #474747;
    --mist: #d9d9d9;
    --paper: #fafafa;
    --cobalt: #0355a3;
    --cobalt-light: #1a6cc0;
    --charcoal-light: #555555;
    --stage: #e6e6e6;
  }
  * { box-sizing: border-box; margin: 0; padding: 0; }
  html, body {
    width: 1200px;
    height: 933px;
    overflow: hidden;
  }
  body {
    position: relative;
    background: var(--stage);
    font-family: "Poiret One", sans-serif;
    color: var(--white);
    text-transform: uppercase;
  }

  .card {
    position: absolute;
    border-radius: 34px;
    padding: 14px;
  }
  .card__face {
    position: relative;
    width: 100%;
    height: 100%;
    border-radius: 22px;
    overflow: hidden;
  }
  .card__pattern {
    position: absolute;
    inset: 0;
  }

  /* Back of card */
  .card--back {
    left: 560px;
    top: 70px;
    width: 560px;
    height: 320px;
    background: var(--cobalt);
  }
  .card--back .card__pattern {
    background: radial-gradient(circle at 60% 45%, var(--charcoal-light), var(--charcoal) 70%);
  }
  .back__content {
    position: absolute;
    inset: 0;
    display: flex;
    flex-direction: column;
    align-items: center;
    justify-content: center;
    gap: 22px;
  }
  .brand {
    display: flex;
    align-items: center;
    gap: 14px;
    color: var(--white);
    letter-spacing: 0.08em;
  }
  .brand__dot {
    flex: none;
    border-radius: 50%;
    background: var(--white);
  }
  .brand--back { font-size: 30px; }
  .brand--back .brand__dot { width: 22px; height: 22px; }
  .back__email {
    font-size: 15px;
    letter-spacing: 0.1em;
  }

  /* Front of card */
  .card--front {
    left: 80px;
    top: 450px;
    width: 700px;
    height: 400px;
    background: var(--ink);
  }
  .card--front .card__pattern {
    background: radial-gradient(circle at 45% 55%, var(--cobalt-light), var(--cobalt) 70%);
  }
  .front__content {
    position: absolute;
    inset: 0;
    display: flex;
    align-items: center;
    padding: 0 40px 0 50px;
  }
  .brand--front {
    font-size: 26px;
    width: 270px;
  }
  .brand--front .brand__dot { width: 18px; height: 18px; }
  .front__divider {
    width: 2px;
    height: 150px;
    background: var(--white);
    margin: 0 26px 0 28px;
  }
  .contact {
    list-style: none;
    font-size: 24px;
    letter-spacing: 0.06em;
    line-height: 1.5;
  }
</style>
</head>
<body>

  <section class="card card--back" aria-label="Card back">
    <div class="card__face">
      <div class="card__pattern" role="img" aria-label="Soft pattern of faint grey circles"></div>
      <div class="back__content">
        <div class="brand brand--back">
          <span class="brand__dot"></span>
          <span class="brand__name">Glazewick Studio</span>
        </div>
        <p class="back__email">Email: Designer@GlazewickStudio.com</p>
      </div>
    </div>
  </section>

  <section class="card card--front" aria-label="Card front">
    <div class="card__face">
      <div class="card__pattern" role="img" aria-label="Soft pattern of faint light-blue circles"></div>
      <div class="front__content">
        <div class="brand brand--front">
          <span class="brand__dot"></span>
          <span class="brand__name">Glazewick Studio</span>
        </div>
        <span class="front__divider"></span>
        <ul class="contact">
          <li class="contact__name">Designer: Hollis Marrow</li>
          <li class="contact__phone">Phone: 418.555.207</li>
        </ul>
      </div>
    </div>
  </section>

</body>
</html>
```